Irish Whiskey Vintage Whiskey Set

Ok, here is an update on my brief for any new or existing designers.
1. This is a luxury gift / packaging and your designs need to reflect that.
2. Just because it is an Irish Whiskey Gift PLEASE do not use any stereotypical motifs etc.
3. Our Logo is attached and we would like to see our logo on the front of the box and Perhaps with the Name "Vintage Whiskey Gift Set"
4. We have attached a Die Cut Box to the specifications required by the manufacturer so the must be followed in order for us to successfully complete the project.
5. We are looking for a classy high end design/ This will be an expensive gift over €200 and the packaging must reflect this.
6. The inside of the box (lid) can simply include the following text about our premises / "1) Nestled in the heart of Galway city’s main shopping thoroughfare, stands the historic building that is Dunmoy’s Public House. An architectural treasure, its current physical footprint dates back to the fortified Galway of 1650. While undergoing some renovations in the offices upstairs, original fireplaces were unearthed and traces of the tower and raw walls from the late Medieval period were also discovered. These precious finds gives one an appreciation why much of it is a protected building. Close your eyes and shut out all ambient noise, and you might even hear a whisper from the ghosts that occupy these walls…
7. Below this text we can use simple numbering and Headers as follows: Vintage Whiskey Number 1 / Vintage Whiskey Number 2 / Vintage Whiskey Number 3.
8. On the back of the box should be a space for a Barcode and I will provide some simple text on the three whiskeys that are in the box.
9. We are not against any embellishments on the box but they must be in a luxurious tasteful designed way.
that’s it, hope everyone understands. Any questions please ask.
We are going to be selling small measures (25ml) of Irish Vintage Whiskey in a new gift box. The gift box will include three Test Tube Like Whiskey Samples of Vintage Irish Whiskey's that are not easily available in any retail or bars for sale. We have a die line for the box from our manufacturere and want someone to create a very dynamic packaging design for the gift set. To be noted, there must be somewhere on the internal display to number the tubes so people can identify the different whiskeys in the tube.
Thats it, hope evryone understands. Any questions please ask.

```html
<!DOCTYPE html>
<html lang="en">
<head>
<meta charset="utf-8">
<title>Dunmoy’s Vintage Whiskey Collection – Box Dieline</title>
<link rel="stylesheet" href="https://fonts.googleapis.com/css2?family=Cormorant+Garamond:wght@600&family=Libre+Caslon+Text&display=swap">
<style>
  :root {
    --bottle-green: #022d17;
    --antique-gold: #b99a34;
    --fold-red: #d3121a;
    --cut-black: #000000;
    --paper: #ffffff;
  }
  html, body {
    margin: 0;
    padding: 0;
    width: 1200px;
    height: 1167px;
    overflow: hidden;
    background: var(--paper);
  }
  .dieline {
    display: block;
    width: 1200px;
    height: 1167px;
  }
  .panel {
    fill: var(--bottle-green);
    stroke: var(--cut-black);
    stroke-width: 1.2;
  }
  .fold-line {
    fill: none;
    stroke: var(--fold-red);
    stroke-width: 1.4;
    stroke-dasharray: 23 24;
  }
  .brand-name {
    fill: var(--antique-gold);
    font-family: "Cormorant Garamond", "Times New Roman", serif;
    font-weight: 600;
    font-size: 78px;
    letter-spacing: 6px;
  }
  .brand-tagline {
    fill: var(--antique-gold);
    font-family: "Libre Caslon Text", "Times New Roman", serif;
    font-size: 15px;
    letter-spacing: 1px;
  }
</style>
</head>
<body>
<svg class="dieline" viewBox="0 0 1200 1167" xmlns="http://www.w3.org/2000/svg" aria-label="Dunmoy’s Vintage Whiskey Collection box dieline">
  <!-- Panels -->
  <rect class="panel panel--top-flap" x="195" y="0.6" width="811" height="191"/>
  <rect class="panel panel--left-side" x="0.6" y="193" width="194.4" height="778"/>
  <rect class="panel panel--right-side" x="1006" y="193" width="193.4" height="778"/>
  <rect class="panel panel--bottom-flap" x="195" y="971" width="811" height="195.4"/>
  <rect class="panel panel--base" x="195" y="191" width="811" height="780" stroke="none"/>

  <!-- Fold lines -->
  <rect class="fold-line" x="195" y="191" width="811" height="779"/>

  <!-- Left side branding (reads bottom to top) -->
  <g class="side-branding side-branding--left" transform="translate(97 585) rotate(-90)">
    <text class="brand-name" x="0" y="26" text-anchor="middle">DUNMOY’S</text>
    <text class="brand-tagline" x="0" y="84" text-anchor="middle">VINTAGE WHISKEY COLLECTION</text>
  </g>

  <!-- Right side branding (reads top to bottom) -->
  <g class="side-branding side-branding--right" transform="translate(1103 585) rotate(90)">
    <text class="brand-name" x="0" y="26" text-anchor="middle">DUNMOY’S</text>
    <text class="brand-tagline" x="0" y="84" text-anchor="middle">VINTAGE WHISKEY COLLECTION</text>
  </g>
</svg>
</body>
</html>
```